Book Cover Design Project - "Pass The Kettle"

"Pass the kettle - crafting tales to lift trade" is a business book that outlines what you need to know if you are planning to make videos for business communications.
The intended audience for the book is small to medium business owners. These are people who are keen to learn what they should know to do it themselves.
The cover needs to have a clear design that works as a thumbnail as well as full size.
Feel free to have some fun with it. It doesn't have to be all serious. Although this is a business book many people are afraid and don't know where to start with video production.
My company logo uses red, black, grey and white - www.brindlemoor.com.au . The logo has been uploaded.
It is not critical to use those elements, however if it can be incorporated into the design that's good too. The priority however is having a design that is eye catching.
The book will about 200 pages long. The back will include an authors photo, so blurb and testimonials- a word doc has been uploaded. It will also include the barcode, ISBN number, and price.
The spine will need to be clear and eyecatching as well.
The design should clearly reveal that this is about video production and provide a feeling of competency and comfort for those who read it.

The dimensions for the cover should be 12.8cm x 19.8cm.

At this point the spine thickness will be about 1.5cm x 19.8cm high

Please include my name on the front cover of the design:

Corin Walsby

The book is targeted to small to medium business owners who want to know how to make videos for their business. They are do it yourself people.

Business

• Front
Title: Pass the kettle
Tagline: Crafting tales to lift trade

I would also like the spine and back cover done as part of the design, however let's get the front done and then the rest can be completed based on the approved design.
• Pass the kettle is a play on words in regards to being filmed (shot) and the anxiety people feel about presenting in front of a camera.
One idea I've had (but I'm not attached to it), is to make the markings that are present in a camera's viewfinder to resemble those that are seen through the sights of a gun.
I'm really not attached to it and unless that can be achieved in a playful way, it is probably best to avoid.
• Please avoid images of low budget cameras. The impression we want here is that this is professional standard video production advice. (By the way you don't have to have any cameras at all).

Low budget cameras are handycams etc.

```html
<!DOCTYPE html>
<html lang="en">
<head>
<meta charset="utf-8">
<title>Pass The Kettle – Book Cover</title>
<link rel="stylesheet" href="https://fonts.googleapis.com/css2?family=Anton&family=Oswald:wght@500;700&family=Open+Sans:wght@400;600&display=swap">
<style>
  :root {
    --stage: #e4e4e4;
    --ink: #0d0d0d;
    --paper: #ffffff;
    --title-shadow: #8a8a8a;
    --body-text: #d6d6d6;
    --muted: #b4b4b4;
    --sky-top: #3f6f9c;
    --sky-bottom: #b9cde0;
    --hud: #e8e8e8;
  }
  * { margin: 0; padding: 0; box-sizing: border-box; }
  html, body { width: 1200px; height: 800px; overflow: hidden; }
  body { background: var(--stage); font-family: "Open Sans", Arial, sans-serif; }

  .cover-spread {
    position: absolute; left: 162px; top: 80px;
    display: flex; height: 640px;
    box-shadow: 0 14px 30px rgba(0,0,0,0.25);
  }

  /* Back cover */
  .back-cover {
    width: 414px; height: 640px; background: var(--ink);
    padding: 26px 22px 20px; position: relative; color: var(--body-text);
  }
  .back-title {
    font-family: "Anton", Impact, sans-serif; color: var(--paper);
    text-align: center; text-transform: uppercase; line-height: 0.95;
    text-shadow: -2px 2px 0 var(--title-shadow); position: relative;
  }
  .back-title .line-one { font-size: 44px; display: block; }
  .back-title .line-two { font-size: 60px; display: block; }
  .back-title .vertical-author {
    position: absolute; left: 72px; bottom: 6px;
    writing-mode: vertical-rl; transform: rotate(180deg);
    font-family: "Oswald", Arial, sans-serif; font-weight: 700;
    font-size: 8px; letter-spacing: 0.5px; text-shadow: none;
  }
  .back-tagline {
    font-family: "Oswald", Arial, sans-serif; font-weight: 700;
    color: var(--paper); font-size: 11px; letter-spacing: 1.8px;
    text-align: center; text-transform: uppercase; margin: 4px 0 10px;
  }
  .back-blurb p {
    font-size: 8.6px; line-height: 1.38; text-align: justify; margin-bottom: 3px;
  }
  .back-blurb .credit { padding-left: 6px; }
  .publisher-name {
    position: absolute; left: 24px; bottom: 22px;
    font-family: "Oswald", Arial, sans-serif; font-weight: 500;
    color: var(--muted); font-size: 14px; letter-spacing: 1px; text-transform: uppercase;
  }

  /* Spine */
  .spine {
    width: 48px; height: 640px; background: var(--ink);
    border-left: 1px solid #262626; border-right: 1px solid #262626;
    display: flex; flex-direction: column; align-items: center;
    justify-content: space-between; padding: 22px 0 24px;
  }
  .spine-title {
    writing-mode: vertical-rl; font-family: "Anton", Impact, sans-serif;
    color: var(--paper); font-size: 30px; letter-spacing: 1px; text-transform: uppercase;
    text-shadow: 2px 2px 0 var(--title-shadow);
  }
  .spine-author {
    writing-mode: vertical-rl; font-family: "Oswald", Arial, sans-serif; font-weight: 700;
    color: var(--paper); font-size: 11px; letter-spacing: 1px; text-transform: uppercase;
  }

  /* Front cover */
  .front-cover {
    width: 414px; height: 640px; background: var(--ink); position: relative;
    padding: 38px 16px 0;
  }
  .front-title {
    font-family: "Anton", Impact, sans-serif; color: var(--paper);
    text-align: center; text-transform: uppercase; line-height: 1.02;
    text-shadow: -3px 3px 0 var(--title-shadow), -5px 5px 0 #555;
  }
  .front-title .line-one { display: block; font-size: 100px; }
  .front-title .line-two { display: block; font-size: 138px; }
  .front-tagline {
    font-family: "Oswald", Arial, sans-serif; font-weight: 700; color: var(--paper);
    font-size: 17px; letter-spacing: 2.4px; text-align: center; text-transform: uppercase;
    margin-top: 4px;
  }
  .viewfinder {
    margin-top: 12px; height: 196px; border-radius: 6px; border: 2px solid #3a3a3a;
    background: linear-gradient(180deg, var(--sky-top), var(--sky-bottom));
  }
  .viewfinder-readout {
    display: flex; align-items: center; justify-content: center; gap: 12px;
    margin-top: 8px; font-family: "Oswald", Arial, sans-serif; font-weight: 500;
    color: var(--hud); font-size: 13px; letter-spacing: 1px;
  }
  .viewfinder-readout .rec { width: 8px; height: 8px; border-radius: 50%; background: var(--hud); }
  .front-author {
    position: absolute; left: 0; right: 0; bottom: 22px; text-align: center;
    font-family: "Oswald", Arial, sans-serif; font-weight: 700; color: var(--paper);
    font-size: 13px; letter-spacing: 1px; text-transform: uppercase;
  }
</style>
</head>
<body>
  <main class="cover-spread">
    <section class="back-cover">
      <h2 class="back-title">
        <span class="line-one">Pass The</span>
        <span class="line-two">Kettle</span>
        <span class="vertical-author">Corin Walsby</span>
      </h2>
      <p class="back-tagline">Crafting tales to lift trade</p>
      <div class="back-blurb">
        <p>Are you ready to use online video to propel your business? Are you already using it but with limited success? Or worse are you using video that damages your brand.</p>
        <p>Online video is here to stay and if you are serious about being in business you need to be watched and be watchable.</p>
        <p>With online video you only have a few seconds to grab the attention of your audience. And once you have their attention how do you maintain it and convert that interest into business for you?</p>
        <p>Pass the kettle outlines what's happening in the online world of video and how to make videos that engage your audience. The easy to read structure of this book allows you to jump to the section most relevant for you.</p>
        <p>In 2012, video accounted for 54% of internet traffic. In 2014 it will be 90%. This book outlines how to make videos that stand out from the noise and what types of productions are most suited to you and your business.</p>
        <p>Quality video productions don't just happen by accident.</p>
        <p>With over 20 years in the game, Corin's condensed knowledge of his industry, compiled in this book, will be invaluable to businesses ready to embrace the power of video.</p>
        <p class="credit">- Darla Pennick, Harbour Local Presenter</p>
        <p>This book is the ultimate guide for creating great business videos</p>
        <p class="credit">- Milo Fenwick, Creative Director, Quillstone Communications</p>
        <p>Pass the kettle is a must read for business owners looking to boost their business through video.</p>
        <p class="credit">- Tobias Renner, author of The Seven Rules for Trade Owners' series of business books.</p>
      </div>
      <p class="publisher-name">Brindlemoor</p>
    </section>

    <section class="spine">
      <span class="spine-title">Pass The Kettle</span>
      <span class="spine-author">Corin Walsby</span>
    </section>

    <section class="front-cover">
      <h1 class="front-title">
        <span class="line-one">Pass The</span>
        <span class="line-two">Kettle</span>
      </h1>
      <p class="front-tagline">Crafting tales to lift trade</p>
      <div class="viewfinder" role="img" aria-label="Camera viewfinder scene: a businessman riding a red upward arrow through a blue sky, with focus markings overlaid"></div>
      <div class="viewfinder-readout">
        <span class="rec"></span>
        <span>88.86"</span>
        <span>8.8</span>
        <span>P S A M</span>
        <span>88.88</span>
        <span>88.8K</span>
      </div>
      <p class="front-author">Corin Walsby</p>
    </section>
  </main>
</body>
</html>
```